Postcard Design Project

We are a small printing company specializing in envelope printing.
We market to churches and medical offices.

Industry/Entity Type

It Company

```html
<!DOCTYPE html>
<html lang="en">
<head>
<meta charset="utf-8">
<title>Tessavane Print — Envelope Printing Postcard</title>
<link rel="stylesheet" href="https://fonts.googleapis.com/css2?family=Open+Sans:wght@400;700;800&display=swap">
<style>
  :root {
    --page-bg: #e6e6e6;
    --brand-blue: #0092c8;
    --band-blue: #0193c9;
    --ink: #231f20;
    --white: #ffffff;
    --paper-light: #f4f4f4;
    --paper-mid: #d9d9d9;
    --env-green: #27e07f;
    --env-purple: #7b2ee6;
    --env-yellow: #f0ca24;
    --env-sky: #2e95e6;
  }
  * { box-sizing: border-box; margin: 0; padding: 0; }
  html, body {
    width: 1200px; height: 926px; overflow: hidden;
    background: var(--page-bg);
    font-family: "Open Sans", Arial, sans-serif;
  }
  .postcard {
    position: absolute; left: 40px; top: 90px;
    width: 1120px; height: 747px;
    overflow: hidden; background: var(--paper-light);
  }
  .envelope-backdrop {
    position: absolute; inset: 0 0 154px 0;
    background: radial-gradient(ellipse at 50% 45%, var(--paper-light) 0%, #e8e8e8 60%, var(--paper-mid) 100%);
  }
  .accent-envelope { position: absolute; border-radius: 4px; box-shadow: 4px 6px 10px rgba(0,0,0,.3); }
  .accent-envelope.green  { left: -10px; top: 95px;  width: 130px; height: 140px; background: var(--env-green);  transform: rotate(4deg); }
  .accent-envelope.purple { left: 15px;  top: 220px; width: 225px; height: 150px; background: var(--env-purple); transform: rotate(-4deg); }
  .accent-envelope.yellow { left: 1000px; top: 55px; width: 160px; height: 130px; background: var(--env-yellow); transform: rotate(-14deg); }
  .accent-envelope.sky    { left: 955px; top: 180px; width: 210px; height: 150px; background: var(--env-sky);    transform: rotate(14deg); }

  .headline {
    position: absolute; left: 0; right: 0; top: 42px;
    text-align: center;
    font-weight: 800; font-size: 86px; line-height: 83px;
    letter-spacing: -2px; color: var(--brand-blue);
    text-shadow: 3px 3px 0 var(--ink);
  }
  .subhead {
    position: absolute; left: 150px; right: 0; top: 310px;
    text-align: center;
    font-weight: 800; font-size: 38px; line-height: 43px;
    color: var(--ink);
  }
  .service-list {
    position: absolute; left: 0; right: 0; top: 448px;
    list-style: none; text-align: center;
    font-size: 29px; line-height: 37px; color: var(--ink);
  }
  .service-list li { display: inline-block; margin: 0 6px; }
  .service-list li::before {
    content: ""; display: inline-block;
    width: 20px; height: 20px; margin-right: 8px;
    border: 4px solid var(--brand-blue); background: var(--white);
    vertical-align: -1px;
  }
  .contact-band {
    position: absolute; left: 0; right: 0; bottom: 0; height: 154px;
    background: var(--band-blue); color: var(--white);
  }
  .contact-details {
    position: absolute; left: 50px; top: 36px;
    font-size: 34px; line-height: 44px;
  }
  .contact-details strong { font-weight: 700; }
  .brand-name {
    position: absolute; left: 755px; top: 38px;
    width: 321px; height: 76px;
    border: 3px solid var(--ink); background: var(--white);
    display: flex; align-items: center; justify-content: center;
    font-weight: 800; font-size: 32px; color: var(--ink); letter-spacing: 1px;
    white-space: nowrap;
  }
</style>
</head>
<body>
  <main class="postcard">
    <div class="envelope-backdrop" role="img" aria-label="Photo of overlapping white envelopes"></div>
    <div class="accent-envelope green"  role="img" aria-label="Green envelope"></div>
    <div class="accent-envelope purple" role="img" aria-label="Purple envelope"></div>
    <div class="accent-envelope yellow" role="img" aria-label="Yellow envelope"></div>
    <div class="accent-envelope sky"    role="img" aria-label="Blue envelope"></div>

    <h1 class="headline">DOWN TO YOUR LAST<br>BOX OF ENVELOPES?<br>NO PROBLEM.</h1>
    <p class="subhead">CALL TESSAVANE PRINT FOR FAST,<br>ECONOMICAL, QUALITY ENVELOPES.</p>

    <ul class="service-list">
      <li>Custom Business Envelopes</li><li>Free Copy Changes</li><br>
      <li>Church Offering Envelopes</li><li>Variety of Paper and Size Options</li><br>
      <li>Medical Billing Envelopes</li><li>Free Shipping</li>
    </ul>

    <footer class="contact-band">
      <p class="contact-details">Call for a free estimate <strong>555-014-2380</strong> or<br>E-mail <strong>orders@tessavane.example</strong></p>
      <div class="brand-name">TESSAVANE PRINT</div>
    </footer>
  </main>
</body>
</html>
```